Creative lead conversion landing page for SMBs

We have an AI chatbot webpage for a real estate agent, and we’re are going to start sending traffic to that webpage (primarily from Zorvane)
We want to maximize the percentage of visitors who start conversations with the chatbot.
We have a specific area of the webpage where we can include any HTML.
We need the design and HTML for both desktop and mobile version.
We’re looking for the best designs that help convert visitors into people who engage the chatbot.

Details are in the attached document "Artquilly project for chat conversion". Please let me know if you have any questions!

Target Market(s)

SMBs (think real estate agents, or home services like tree care, housekeepers, electricians, general contractors) will be selling to consumers

Number of Pages Required

1 page

Font styles to use
Other font styles liked:
• Zorvane Poppins

Requirements
Must have
• Creative design that catches users eyes and with good content (content of course out of scope) will encourage a user to want to learn more.

```html
<!DOCTYPE html>
<html lang="en">
<head>
<meta charset="utf-8">
<title>Nestora – Real Estate Agent</title>
<link href="https://fonts.googleapis.com/css2?family=Poppins:wght@400;500;600;700&display=swap" rel="stylesheet">
<style>
:root{
  --navy:#0b1434;
  --navy-2:#18213f;
  --strip:#c9d0dc;
  --purple:#6e56b8;
  --purple-2:#9a5fa8;
  --blue:#4a63b4;
  --ink:#1b1d2a;
  --muted:#7a6fa0;
  --line:#e3e4ea;
  --bubble:#eef0f4;
  --lav:#eceefb;
  --gold:#f4c245;
  --teal:#1aa5c6;
}
*{box-sizing:border-box;margin:0;padding:0}
html,body{width:874px;height:1200px;overflow:hidden;background:#fff}
body{font-family:'Poppins',sans-serif;color:var(--ink)}
.stage{position:absolute;left:0;top:0;width:1366px;height:1876px;transform:scale(0.6398);transform-origin:0 0}
.abs{position:absolute}
.sidebar{left:0;top:0;width:252px;height:1876px;background:var(--navy)}
.sidebar-edge{left:252px;top:0;width:5px;height:1876px;background:var(--strip)}
.brand{left:0;width:252px;top:14px;text-align:center;color:#fff;font-weight:700;font-size:36px;letter-spacing:.5px}
.avatar{border-radius:50%;background:linear-gradient(160deg,#5a4636,#c9a48a 60%,#efe6de)}
.agent-side-name{left:0;width:252px;top:157px;text-align:center;color:var(--purple);font-size:20px;font-weight:500}
.agent-side-role{left:0;width:252px;top:183px;text-align:center;color:#8c8fa8;font-size:12px;font-weight:500}
.talk{left:27px;top:240px;color:#fff;font-size:14px;white-space:nowrap}
.nav-item{left:21px;width:220px;height:43px;display:flex;align-items:center;gap:14px;padding-left:12px;color:#fff;font-size:14px;white-space:nowrap}
.nav-item.active{width:208px;background:var(--navy-2);border-radius:6px;color:var(--purple)}
.nav-item.purple{color:var(--purple)}
.nav-bar{left:0;top:298px;width:3px;height:43px;background:var(--purple)}
.cta-side{left:21px;top:1726px;width:205px;height:42px;border-radius:6px;background:linear-gradient(90deg,var(--blue),var(--purple-2));color:#fff;font-size:13px;font-weight:600;display:flex;align-items:center;justify-content:center;white-space:nowrap}
.copy{left:19px;top:1822px;color:var(--purple);font-size:11px}
.social{top:1820px;width:14px;height:14px;border-radius:50%;background:var(--purple)}
.topbar{left:257px;top:0;width:1109px;height:52px;border-bottom:1px solid var(--line)}
.top-group{left:277px;top:10px;height:26px;display:flex;align-items:center;gap:12px;white-space:nowrap}
.top-mark{width:28px;height:24px;border-radius:50%;background:var(--purple)}
.top-name{font-size:17px;font-weight:600}
.pill-link{height:26px;padding:0 8px;border:1px solid var(--purple);border-radius:5px;color:var(--purple);font-size:12px;display:flex;align-items:center;margin-left:2px}
.title{left:257px;width:1109px;top:78px;text-align:center;font-size:40px;font-weight:500;background:linear-gradient(90deg,var(--purple),var(--purple-2));-webkit-background-clip:text;background-clip:text;color:transparent}
.hero{left:315px;top:194px;width:390px;height:200px;border-radius:10px;background:linear-gradient(180deg,#24241e 0%,#6b5a3a 40%,#c9a86a 60%,#3cb2c9 85%,#2a6f7a 100%)}
.offer{left:634px;top:212px;width:58px;height:24px;border-radius:4px;background:var(--teal);color:#fff;font-size:14px;font-weight:600;display:flex;align-items:center;justify-content:center}
.prop-name{left:738px;top:194px;font-size:20px;font-weight:500}
.feat-ico{left:738px}
.feat-title{font-size:14px;font-weight:500}
.feat-desc{font-size:14px;white-space:nowrap}
.h-photos{left:317px;top:444px;font-size:18px;font-weight:500}
.thumb{top:486px;width:240px;height:140px;border-radius:6px}
.divider{left:315px;width:1002px;height:1px;background:var(--line)}
.agent-name{left:394px;top:704px;font-size:17px;font-weight:500}
.agent-role{left:395px;top:734px;font-size:12px;color:var(--muted);font-weight:500}
.rev-count{left:314px;top:780px;display:flex;align-items:center;gap:12px;font-size:14px}
.bio{left:314px;top:809px;width:480px;font-size:14px;line-height:20px}
.more{left:315px;top:916px;font-size:14px;font-weight:500;text-decoration:underline}
.fact{left:884px;font-size:14px;white-space:nowrap}
.rev-head{left:314px;top:994px;display:flex;align-items:center;gap:10px;font-size:20px;font-weight:500}
.review{width:480px}
.review .r-ava{position:absolute;left:0;top:0;width:40px;height:40px;border-radius:50%}
.review .r-name{position:absolute;left:52px;top:-4px;font-size:16px;font-weight:500}
.review .r-date{position:absolute;left:52px;top:18px;font-size:16px;color:var(--muted)}
.review .r-stars{position:absolute;left:0;top:46px;display:flex;gap:3px}
.review .r-title{position:absolute;left:0;top:68px;font-size:15px;font-weight:500}
.review .r-body{position:absolute;left:0;top:97px;width:475px;font-size:14px;line-height:20px}
.show-all{left:315px;top:1468px;width:170px;height:42px;border-radius:5px;background:linear-gradient(90deg,var(--blue),var(--purple-2));color:#fff;font-size:14px;font-weight:600;display:flex;align-items:center;justify-content:center}
.bubble{left:315px;top:1566px;width:610px;height:100px;border-radius:16px;background:var(--bubble);padding:8px 18px;font-size:15px;line-height:23px;color:#3b3e4c}
.bubble-tail{left:336px;top:1664px}
.mascot{left:326px;top:1682px;width:34px;height:38px;border-radius:50% 50% 45% 45%;background:linear-gradient(180deg,#7fd2ea,#3fa6cf)}
.chat-panel{left:316px;top:1732px;width:949px;height:103px;border-radius:8px;border:1px solid var(--line);overflow:hidden}
.chat-meta{position:absolute;left:0;top:0;width:100%;height:41px;background:var(--lav)}
.meta-label{position:absolute;left:12px;top:12px;font-size:12px}
.meta-pill{position:absolute;background:#fff;border-radius:4px;height:24px;top:8px;display:flex;align-items:center;padding-left:8px;font-size:13px;white-space:nowrap}
.new-prompt{position:absolute;left:650px;top:12px;font-size:12px;color:var(--purple)}
.chat-input{position:absolute;left:0;top:41px;width:100%;height:62px;background:#fff}
.plus{position:absolute;left:16px;top:18px;font-size:16px;color:#555}
.placeholder{position:absolute;left:41px;top:17px;font-size:18px;color:#8a8d99}
.counter{left:1160px;width:83px;top:1842px;text-align:right;font-size:12px;color:#555}
</style>
</head>
<body>
<div class="stage">
  <aside class="abs sidebar"></aside>
  <div class="abs sidebar-edge"></div>
  <div class="abs brand">Nestora</div>
  <div class="abs avatar" style="left:92px;top:83px;width:66px;height:66px" role="img" aria-label="Portrait photo of the agent"></div>
  <div class="abs agent-side-name">Marisol</div>
  <div class="abs agent-side-role">Real Estate Agent</div>
  <div class="abs talk">Talk to Nestora, my AI assistant</div>

  <div class="abs nav-bar"></div>
  <div class="abs nav-item active" style="top:298px">
    <svg width="22" height="18" viewBox="0 0 22 18"><ellipse cx="8" cy="7" rx="7" ry="6" fill="#6e56b8"/><ellipse cx="15" cy="11" rx="6" ry="5" fill="#4a63b4"/></svg>
    Nestora Talk
  </div>
  <div class="abs nav-item purple" style="top:357px">
    <svg width="22" height="22" viewBox="0 0 22 22" fill="none" stroke="#6e56b8" stroke-width="1.4"><path d="M3 10 L11 3 L19 10 V19 H3 Z"/><circle cx="11" cy="13" r="3"/><path d="M13 15 L16 18"/></svg>
    Search for real estate
  </div>
  <div class="abs nav-item" style="top:414px">
    <svg width="22" height="22" viewBox="0 0 22 22" fill="none" stroke="#6e56b8" stroke-width="1.6"><circle cx="11" cy="11" r="9" fill="#6e56b8" fill-opacity=".35"/><path d="M2 11 H20 M11 2 C6 7 6 15 11 20 M11 2 C16 7 16 15 11 20"/></svg>
    Things to do in Elmdale
  </div>
  <div class="abs nav-item" style="top:469px">
    <svg width="22" height="22" viewBox="0 0 22 22" fill="none" stroke="#6e56b8" stroke-width="1.4"><rect x="2" y="3" width="18" height="15" rx="2"/><path d="M11 6 L12.5 9.5 L16 10 L13.3 12.2 L14.2 15.5 L11 13.6 L7.8 15.5 L8.7 12.2 L6 10 L9.5 9.5 Z"/></svg>
    Reviews/testimonials
  </div>

  <div class="abs cta-side">Create your own free Nestora</div>
  <div class="abs copy">© 2023 Nestora.ai</div>
  <div class="abs social" style="left:153px"></div>
  <div class="abs social" style="left:180px"></div>
  <div class="abs social" style="left:207px"></div>

  <header class="abs topbar"></header>
  <div class="abs top-group">
    <div class="top-mark"></div>
    <div class="top-name">Nestora Talk</div>
    <div class="pill-link">Prompts library</div>
  </div>

  <h1 class="abs title">Welcome to Nestora</h1>

  <div class="abs hero" role="img" aria-label="Photo of a villa with a lit pool at night"></div>
  <div class="abs offer">OFFER</div>

  <div class="abs prop-name">Cedar Hollow Retreat</div>
  <svg class="abs feat-ico" style="top:235px" width="26" height="24" viewBox="0 0 26 24" fill="none" stroke="#222" stroke-width="1.3"><path d="M2 12 H24 V17 H2 Z M5 17 V22 M21 17 V22 M4 12 V3 M4 5 H9 M18 12 V6 H23 V12"/></svg>
  <div class="abs feat-title" style="left:796px;top:236px">Dedicated workspace</div>
  <div class="abs feat-desc" style="left:796px;top:257px">A room with wifi that’s well-suited for working.</div>
  <svg class="abs feat-ico" style="top:290px" width="24" height="22" viewBox="0 0 24 22" fill="none" stroke="#222" stroke-width="1.3"><path d="M2 8 Q6 5 10 8 T20 8 M2 13 Q6 10 10 13 T20 13 M2 18 Q6 15 10 18 T20 18 M8 2 V16 M15 2 V16"/></svg>
  <div class="abs feat-title" style="left:793px;top:289px">Dive right in</div>
  <div class="abs feat-desc" style="left:793px;top:310px">This is one of the few places in the area with a pool.</div>
  <svg class="abs feat-ico" style="top:342px" width="26" height="26" viewBox="0 0 26 26" fill="none" stroke="#222" stroke-width="1.4"><path d="M3 6 H17 M3 6 V19 H8 L8 24 L13 19 H21 V12"/><circle cx="21" cy="5" r="3"/></svg>
  <div class="abs feat-title" style="left:794px;top:344px">Great communication</div>
  <div class="abs feat-desc" style="left:794px;top:365px">90% of recent clients rated Marisol 5 stars for communication.</div>

  <h2 class="abs h-photos">Photos</h2>
  <div class="abs thumb" style="left:315px;background:linear-gradient(160deg,#d9c3a0,#a58459 50%,#ece7dd)" role="img" aria-label="Photo of a bedroom"></div>
  <div class="abs thumb" style="left:568px;background:linear-gradient(160deg,#e9e4dc,#b89a76 55%,#8b6a48)" role="img" aria-label="Photo of a kitchen"></div>
  <div class="abs thumb" style="left:821px;background:linear-gradient(160deg,#f1ede6,#d9d2c8 55%,#5a3a2c)" role="img" aria-label="Photo of a bathroom"></div>
  <div class="abs thumb" style="left:1076px;background:linear-gradient(160deg,#ede8df,#9a8a78 55%,#c8b69a)" role="img" aria-label="Photo of a living room"></div>

  <div class="abs divider" style="top:662px"></div>

  <div class="abs avatar" style="left:315px;top:690px;width:66px;height:66px" role="img" aria-label="Portrait photo of the agent"></div>
  <div class="abs agent-name">Marisol</div>
  <div class="abs agent-role">Real Estate Agent</div>
  <div class="abs rev-count">
    <svg width="16" height="16" viewBox="0 0 24 24"><path fill="#1b1d2a" d="M12 2 L15 9 L22 9.5 L16.5 14 L18.5 21 L12 17 L5.5 21 L7.5 14 L2 9.5 L9 9 Z"/></svg>
    22 Reviews
  </div>
  <p class="abs bio">Hello! I'm Marisol, a passionate real estate agent with an unwavering commitment to helping you find your dream home. With years of experience in the real estate market, I am dedicated to providing you with exceptional service and making your buying or selling experience as smooth and successful as possible.</p>
  <div class="abs more">More information ›</div>
  <div class="abs fact" style="top:779px">Real estate agent registration number: 238417</div>
  <div class="abs fact" style="top:816px">Languages: English, Español</div>
  <div class="abs fact" style="top:852px">Response rate: 100%</div>
  <div class="abs fact" style="top:888px">Response time: immediately with my AI assistant</div>

  <div class="abs divider" style="top:965px"></div>

  <h2 class="abs rev-head">
    <svg width="16" height="16" viewBox="0 0 24 24"><path fill="#1b1d2a" d="M12 2 L15 9 L22 9.5 L16.5 14 L18.5 21 L12 17 L5.5 21 L7.5 14 L2 9.5 L9 9 Z"/></svg>
    22 Reviews
  </h2>

  <svg width="0" height="0" style="position:absolute"><defs><symbol id="star" viewBox="0 0 24 24"><path fill="#f4c245" d="M12 2 L15 9 L22 9.5 L16.5 14 L18.5 21 L12 17 L5.5 21 L7.5 14 L2 9.5 L9 9 Z"/></symbol></defs></svg>

  <article class="abs review" style="left:314px;top:1046px">
    <div class="r-ava" style="background:linear-gradient(160deg,#d8c8b6,#8a7664)" role="img" aria-label="Reviewer photo"></div>
    <div class="r-name">Dalia Fenwick</div>
    <div class="r-date">July 2023</div>
    <div class="r-stars"><svg width="14" height="14"><use href="#star"/></svg><svg width="14" height="14"><use href="#star"/></svg><svg width="14" height="14"><use href="#star"/></svg><svg width="14" height="14"><use href="#star"/></svg><svg width="14" height="14"><use href="#star"/></svg></div>
    <div class="r-title">Marisol was amazing.</div>
    <p class="r-body">She helped me find my very first home! With me being a first time homebuyer I had several questions about how everything would work and she would always answer them or find me the answer if she didn’t know the answer right away. I would highly recommend her to anyone that is looking to buy or sell a home</p>
  </article>

  <article class="abs review" style="left:849px;top:1046px">
    <div class="r-ava" style="background:linear-gradient(160deg,#4a3a30,#1e1a18)" role="img" aria-label="Reviewer photo"></div>
    <div class="r-name">Corwin</div>
    <div class="r-date">February 2023</div>
    <div class="r-stars"><svg width="14" height="14"><use href="#star"/></svg><svg width="14" height="14"><use href="#star"/></svg><svg width="14" height="14"><use href="#star"/></svg><svg width="14" height="14"><use href="#star"/></svg><svg width="14" height="14"><use href="#star"/></svg></div>
    <div class="r-title">Marisol is great!</div>
    <p class="r-body">She is organized, attentive, happy, and goes the proverbial extra mile. I had little time for the purchase and often times was messaging Marisol last minute to see a listing. She made it work every time and made my home buying process way easier than I could have expected.</p>
  </article>

  <article class="abs review" style="left:314px;top:1277px">
    <div class="r-ava" style="background:linear-gradient(160deg,#c46a3a,#6a3a22)" role="img" aria-label="Reviewer photo"></div>
    <div class="r-name">Tobias and Wren</div>
    <div class="r-date">August 2023</div>
    <div class="r-stars" style="top:44px"><svg width="14" height="14"><use href="#star"/></svg><svg width="14" height="14"><use href="#star"/></svg><svg width="14" height="14"><use href="#star"/></svg><svg width="14" height="14"><use href="#star"/></svg><svg width="14" height="14"><use href="#star"/></svg></div>
    <div class="r-title" style="top:65px">Marisol is the best!</div>
    <p class="r-body" style="top:93px">She was extremely helpful to me and my girlfriend as First Time Homebuyers. She made the whole process super easy and stress free :)</p>
  </article>

  <article class="abs review" style="left:849px;top:1277px">
    <div class="r-ava" style="background:linear-gradient(160deg,#b8a08a,#3a2e28)" role="img" aria-label="Reviewer photo"></div>
    <div class="r-name">Idris Calloway</div>
    <div class="r-date">August 2023</div>
    <div class="r-stars" style="top:44px"><svg width="14" height="14"><use href="#star"/></svg><svg width="14" height="14"><use href="#star"/></svg><svg width="14" height="14"><use href="#star"/></svg><svg width="14" height="14"><use href="#star"/></svg><svg width="14" height="14"><use href="#star"/></svg></div>
    <div class="r-title" style="left:-2px;top:65px">Marisol was incredible!</div>
    <p class="r-body" style="left:-1px;top:93px">Your first home buying experience can be intimidating, but she was with us each step of the way to thoroughly explain the process. She wanted us to find a house that was the right fit for us, and listened to our needs. I’d recommend working with Marisol to anyone!</p>
  </article>

  <div class="abs show-all">Show all reviews</div>

  <div class="abs bubble">Hi! I'm the AI assistant to Marisol, who can help you buy or sell a home in the Brookhaven area. I am happy to help get you connected to her. First, what's your name?</div>
  <svg class="abs bubble-tail" width="16" height="12" viewBox="0 0 16 12"><path d="M0 0 H16 L8 10 Z" fill="#eef0f4"/></svg>
  <div class="abs mascot" role="img" aria-label="Small bird mascot illustration"></div>

  <div class="abs chat-panel">
    <div class="chat-meta">
      <span class="meta-label">Current personality:</span>
      <span class="meta-pill" style="left:139px;width:178px;font-weight:500">Real Estate Agent</span>
      <span class="new-prompt">+ New prompt</span>
      <span class="meta-pill" style="left:750px;width:177px;padding-left:16px;font-size:12px">Charge: 2 output words</span>
    </div>
    <div class="chat-input">
      <span class="plus">+</span>
      <span class="placeholder">Type your response...</span>
      <svg style="position:absolute;left:905px;top:20px" width="22" height="20" viewBox="0 0 22 20" fill="none" stroke="#8f86c9" stroke-width="1.4"><path d="M1 1 L21 10 L1 19 L4 10 Z M4 10 H12"/></svg>
    </div>
  </div>
  <svg class="abs" style="left:1293px;top:1790px" width="20" height="28" viewBox="0 0 20 28"><rect x="6" y="1" width="8" height="16" rx="4" fill="#6e56b8"/><path d="M2 12 Q2 21 10 21 Q18 21 18 12 M10 21 V26 M6 26 H14" fill="none" stroke="#6e56b8" stroke-width="2"/></svg>
  <div class="abs counter">0 / 4000</div>
</div>
</body>
</html>
```